Business Card Design Project

Need a business card that stands my education platform as a whole but

Target Market(s)

Parents, families, expats in the middle east.

Industry/Entity Type

Education

Contact Information for Business Card

www.brightsprout.ae
www.thehomenest.ae
www.thecarecirclehub.ae

+971543192704
rebecca@brightsprout.ae

Font styles to use
Serif

Requirements
Must have
• Logo's and contact details

```html
<!DOCTYPE html>
<html lang="en">
<head>
<meta charset="utf-8">
<title>Bright Sprout — Business Card</title>
<link rel="stylesheet" href="https://fonts.googleapis.com/css2?family=Crimson+Text:wght@400;600&display=swap">
<style>
  :root {
    --backdrop: #d4d4d4;
    --card: #36312f;
    --teal: #3a7c94;
    --orange: #e8884a;
    --white: #ffffff;
    --serif: "Crimson Text", Georgia, serif;
  }
  * { margin: 0; padding: 0; box-sizing: border-box; }
  html, body { width: 1200px; height: 1000px; overflow: hidden; }
  body { position: relative; background: var(--backdrop); font-family: var(--serif); }

  .card {
    position: absolute;
    left: 322px;
    width: 558px;
    height: 350px;
    background: var(--card);
    border-radius: 28px;
    overflow: hidden;
  }
  .card--front { top: 120px; }
  .card--back { top: 530px; }

  .brand {
    position: absolute;
    display: flex;
    align-items: center;
    gap: 10px;
    color: var(--white);
    font-family: var(--serif);
    font-weight: 600;
    white-space: nowrap;
  }
  .brand__dot {
    display: block;
    border-radius: 50%;
    background: var(--teal);
    flex: none;
  }
  .card--front .brand {
    left: 50%;
    top: 175px;
    transform: translate(-50%, -50%);
    font-size: 34px;
  }
  .card--front .brand__dot { width: 22px; height: 22px; }

  .card--back .brand {
    left: 128px;
    top: 175px;
    transform: translate(-50%, -50%);
    font-size: 24px;
    gap: 8px;
  }
  .card--back .brand__dot { width: 16px; height: 16px; }

  .contact-panel {
    position: absolute;
    left: 263px;
    top: 93px;
    width: 295px;
    height: 162px;
    background: var(--teal);
    padding: 22px 0 0 18px;
    color: var(--white);
    font-size: 18px;
    line-height: 22px;
  }
  .contact-panel__accent {
    position: absolute;
    right: 0;
    top: 0;
    width: 18px;
    height: 100%;
    background: var(--orange);
  }
  .contact-panel__group + .contact-panel__group { margin-top: 8px; }
  .contact-panel__line { display: block; }
</style>
</head>
<body>
  <section class="card card--front" aria-label="Card front">
    <div class="brand"><span class="brand__dot"></span>Bright Sprout</div>
  </section>

  <section class="card card--back" aria-label="Card back">
    <div class="brand"><span class="brand__dot"></span>Bright Sprout</div>
    <div class="contact-panel">
      <div class="contact-panel__group">
        <span class="contact-panel__line">www.brightsprout.ae</span>
        <span class="contact-panel__line">www.thehomenest.ae</span>
        <span class="contact-panel__line">www.thecarecirclehub.ae</span>
      </div>
      <div class="contact-panel__group">
        <span class="contact-panel__line">+971543192704</span>
        <span class="contact-panel__line">rebecca@brightsprout.ae</span>
      </div>
      <span class="contact-panel__accent"></span>
    </div>
  </section>
</body>
</html>
```